Wandrift: Travel business card redesign

We need a clean elegant look for our cards featuring blue and orange. Look should communicate a sense of strong design and seem uncluttered. The company is Wandrift which means drift to wander. As in every trip is an drift to wander. Feel free to reinvent the logo or just tweak it. Colors should be blue like Caribbean waters and a saturated orange. Keep it clean and simple.
Please match the information in the sample uploaded but the sample is horrible -- a non-starter -- use for information only. also please add managing director to my name as title

Target Market(s)
potential clients, hotels, trade publications
Industry/Entity Type
Travel Industry
Contact Information for Business Card
as above
Requirements
Must have
- Font should be century gothic. Colors below are close but a but prefer lighter in each case.

```html
<!DOCTYPE html>
<html lang="en">
<head>
<meta charset="utf-8">
<title>Wandrift – Business Card</title>
<link rel="stylesheet" href="https://fonts.googleapis.com/css2?family=Didact+Gothic&family=Great+Vibes&display=swap">
<style>
  :root {
    --bg: #ffffff;
    --ink: #1b1b1b;
    --brand-orange: #ef8b2c;
    --band-light: #f6b64a;
    --band-deep: #f3913a;
    --icon-blue: #6aaed6;
    --on-band: #ffffff;
  }
  html, body {
    margin: 0;
    padding: 0;
    overflow: hidden;
    background: var(--bg);
  }
  .card {
    position: relative;
    width: 1200px;
    height: 734px;
    overflow: hidden;
    background: var(--bg);
    font-family: "Didact Gothic", "Century Gothic", sans-serif;
    color: var(--ink);
  }
  .footer-band {
    position: absolute;
    left: 0;
    right: 0;
    bottom: 0;
    height: 126px;
    background: linear-gradient(90deg, var(--band-light), var(--band-deep) 45%, var(--band-deep));
  }
  .wordmark {
    position: absolute;
    left: 92px;
    top: 118px;
    margin: 0;
    font-size: 118px;
    font-weight: 400;
    letter-spacing: -1px;
    line-height: 1;
    color: var(--brand-orange);
  }
  .person {
    position: absolute;
    left: 86px;
    top: 328px;
    margin: 0;
    font-style: italic;
    font-size: 48px;
    line-height: 56px;
    letter-spacing: 1px;
  }
  .person span { display: block; }
  .contact {
    position: absolute;
    left: 646px;
    top: 0;
    margin: 0;
    padding: 0;
    list-style: none;
    font-size: 35px;
  }
  .contact li {
    position: absolute;
    left: 0;
    white-space: nowrap;
  }
  .contact svg {
    position: absolute;
    fill: var(--icon-blue);
  }
  .contact .text {
    position: absolute;
    left: 80px;
    line-height: 42px;
  }
  .contact .address { top: 124px; }
  .contact .address svg { top: 14px; left: 10px; }
  .contact .office { top: 256px; }
  .contact .office svg { top: 0; left: 8px; }
  .contact .mobile { top: 346px; }
  .contact .mobile svg { top: 0; left: 12px; }
  .contact .fax { top: 436px; }
  .contact .fax svg { top: 0; left: 2px; }
  .site {
    position: absolute;
    left: 90px;
    top: 644px;
    font-size: 52px;
    color: var(--on-band);
    line-height: 1;
  }
  .tagline {
    position: absolute;
    right: 22px;
    top: 618px;
    font-family: "Great Vibes", cursive;
    font-size: 84px;
    color: var(--on-band);
    line-height: 1;
  }
</style>
</head>
<body>
<div class="card">
  <div class="footer-band" role="img" aria-label="Warm orange footer band"></div>

  <h1 class="wordmark">wandrift</h1>

  <p class="person">
    <span class="title">Managing Director</span>
    <span class="name">Leo Marlowe</span>
  </p>

  <ul class="contact">
    <li class="address">
      <svg width="34" height="54" viewBox="0 0 34 54" aria-hidden="true">
        <path d="M17 0 C7.6 0 0 7.6 0 17 C0 29 17 54 17 54 C17 54 34 29 34 17 C34 7.6 26.4 0 17 0 Z M17 24 A7 7 0 1 1 17 10 A7 7 0 1 1 17 24 Z"/>
      </svg>
      <span class="text">4120 Coral Reef Lane<br>N. Seabrook, 90512</span>
    </li>
    <li class="office">
      <svg width="40" height="50" viewBox="0 0 40 50" aria-hidden="true">
        <path d="M6 2 L14 0 L18 14 L12 18 C14 26 19 33 26 38 L31 33 L40 42 L36 48 C34 50 30 50 26 48 C13 40 4 26 1 12 C0 8 2 4 6 2 Z"/>
      </svg>
      <span class="text">877.55.DRIFT (37438)</span>
    </li>
    <li class="mobile">
      <svg width="30" height="50" viewBox="0 0 30 50" aria-hidden="true">
        <path d="M4 0 H26 A4 4 0 0 1 30 4 V46 A4 4 0 0 1 26 50 H4 A4 4 0 0 1 0 46 V4 A4 4 0 0 1 4 0 Z M4 6 V40 H26 V6 Z M15 42 A2.5 2.5 0 1 0 15 47 A2.5 2.5 0 1 0 15 42 Z" fill-rule="evenodd"/>
      </svg>
      <span class="text">323.555.0142</span>
    </li>
    <li class="fax">
      <svg width="46" height="44" viewBox="0 0 46 44" aria-hidden="true">
        <rect x="12" y="0" width="22" height="10"/>
        <path d="M4 12 H42 A4 4 0 0 1 46 16 V32 H38 V26 H8 V32 H0 V16 A4 4 0 0 1 4 12 Z"/>
        <rect x="10" y="28" width="26" height="16"/>
        <rect x="14" y="32" width="18" height="2" fill="#fff"/>
        <rect x="14" y="37" width="18" height="2" fill="#fff"/>
      </svg>
      <span class="text">310.555.0187</span>
    </li>
  </ul>

  <div class="site">wandrift.com</div>
  <div class="tagline">drift to wander</div>
</div>
</body>
</html>
```